Northgate Roofing Works Inc Business cards

Commercial and Residential Roofing contractor needs design logo and card design. Can be single or double sided but must incorporate:
Persons Name:
Persons Title:
Mailing Address: PO Box 3719
Physical Address: 58 Fenwick Lane
Harlow, Ma. 01642
800-316-5842
508-712-5842
Fax: 508-712-5867
Cell: Person Cell number
email address
Website: WWW.northgateroofworks.com

Target Market(s)

Residential home owners and commercial building owners

Industry/Entity Type

Roofing

Contact Information for Business Card

Persons Name:
Persons Title:
Harlow, Ma. 01642
800-316-5842
508-712-5842
Fax: 508-712-5867
Cell: Person Cell number
email address

Logo Text

Large enough to service small enough to care

Font styles to use
Serif

Colors
0355a3

Requirements
Must have
• Commercial and Residential Roofing contractor needs design logo and card design. Can be single or double sided but must incorporate:
• Persons Name:
• Persons Title:
• Mailing Address: PO Box 3719
• Physical Address: 58 Fenwick Lane
• Harlow, Ma. 01642
• 800-316-5842
• 508-712-5842
• Fax: 508-712-5867
• Cell: Person Cell number
• email address
• Website: WWW.northgateroofworks.com
Nice to have
• ..
Should not have
• I'm looking for something different. I have had the same card for 23 years. I attached what both sides of my present card looks like.

```html
<!DOCTYPE html>
<html lang="en">
<head>
<meta charset="utf-8">
<title>Northgate Roofing Works – Business Cards</title>
<link rel="stylesheet" href="https://fonts.googleapis.com/css2?family=Ubuntu:wght@400;500;700&display=swap">
<style>
  :root {
    --brand-blue: #0355a3;
    --ink: #3d3b3c;
    --ink-dark: #2b292a;
    --band: #403c3d;
    --faint: #d6d6d6;
    --backdrop: #e8e8e8;
    --paper: #ffffff;
  }
  * { box-sizing: border-box; margin: 0; padding: 0; }
  html, body {
    width: 800px; height: 1200px; overflow: hidden;
    background: var(--backdrop);
    font-family: "Ubuntu", sans-serif;
    color: var(--ink-dark);
  }
  .canvas { position: relative; width: 800px; height: 1200px; }

  .card {
    position: absolute; left: 89px; width: 624px; height: 358px;
    background: var(--paper);
  }
  .card--front { top: 22px; }
  .card--back { top: 470px; overflow: hidden; }

  .wordmark {
    position: absolute; left: 0; right: 0;
    display: flex; align-items: center; justify-content: center; gap: 18px;
  }
  .wordmark__mark { width: 22px; height: 22px; background: var(--brand-blue); flex: none; }
  .wordmark__name {
    font-weight: 400; color: var(--ink); text-align: center;
    font-size: 50px; line-height: 1.1; letter-spacing: 2px;
  }
  .card--front .wordmark { top: 118px; }

  .watermark {
    position: absolute; left: 0; right: 0; top: 256px;
    text-align: center; color: var(--faint);
    font-size: 28px; line-height: 34px; letter-spacing: 2px;
  }

  .person { position: absolute; left: 22px; top: 73px; }
  .person__name { font-size: 21px; font-weight: 700; letter-spacing: 0.5px; }
  .person__title { font-size: 18px; font-weight: 500; margin-top: 2px; }

  .direct { position: absolute; left: 20px; top: 168px; font-size: 15.5px; font-weight: 500; }
  .direct__row { display: flex; align-items: center; gap: 14px; height: 30px; margin-bottom: 18px; }
  .direct__row svg { width: 22px; height: 28px; fill: var(--ink-dark); }

  .office { position: absolute; right: 22px; top: 71px; font-size: 15.5px; font-weight: 500; text-align: right; }
  .office__row { display: flex; align-items: center; justify-content: flex-end; gap: 14px; line-height: 21px; }
  .office__row + .office__row { margin-top: 25px; }
  .office__row svg { width: 22px; height: 22px; fill: var(--ink-dark); flex: none; }

  .web-band {
    position: absolute; left: 0; right: 0; bottom: 0; height: 62px;
    background: var(--band); color: var(--paper);
    display: flex; align-items: center; justify-content: center;
    font-size: 24px; font-weight: 500; letter-spacing: 0.3px;
  }

  .logo-sheet {
    position: absolute; left: 0; top: 933px; width: 800px; height: 267px;
    background: var(--paper);
  }
  .logo-sheet .wordmark { top: 118px; }
</style>
</head>
<body>
<main class="canvas">

  <section class="card card--front" aria-label="Card front">
    <div class="wordmark">
      <span class="wordmark__mark"></span>
      <span class="wordmark__name">NORTHGATE<br>ROOFING WORKS</span>
    </div>
  </section>

  <section class="card card--back" aria-label="Card back">
    <div class="watermark" aria-hidden="true">NORTHGATE ROOFING WORKS</div>

    <div class="person">
      <p class="person__name">DALE KOWALCZYK</p>
      <p class="person__title">President</p>
    </div>

    <div class="direct">
      <div class="direct__row">
        <svg viewBox="0 0 22 28" aria-hidden="true"><path d="M4 1h14a3 3 0 0 1 3 3v20a3 3 0 0 1-3 3H4a3 3 0 0 1-3-3V4a3 3 0 0 1 3-3zm-1 4v17h16V5z"/><circle cx="11" cy="24.5" r="1.3"/></svg>
        <span>508-604-2281</span>
      </div>
      <div class="direct__row">
        <svg viewBox="0 0 22 28" aria-hidden="true"><path d="M1 8h20v13H1zm2 2v.4l8 6 8-6V10zm0 2.9V19h16v-6.1l-8 6z"/></svg>
        <span>dale@northgateroofworks.com</span>
      </div>
    </div>

    <div class="office">
      <div class="office__row">
        <span>58 Fenwick Lane PO Box 3719<br>Harlow, Ma. 01642</span>
        <svg viewBox="0 0 22 22" aria-hidden="true"><path d="M11 2 1 11h3v9h5v-6h4v6h5v-9h3z"/></svg>
      </div>
      <div class="office__row">
        <span>800-316-5842<br>508-712-5842</span>
        <svg viewBox="0 0 22 22" aria-hidden="true"><path d="M2 8c0-3 4-4 9-4s9 1 9 4v2h-5V8H7v2H2zm3 4h12l3 8H2zm6 1.5a2.5 2.5 0 1 0 0 5 2.5 2.5 0 0 0 0-5z"/></svg>
      </div>
      <div class="office__row">
        <span>Fax: 508-712-5867</span>
        <svg viewBox="0 0 22 22" aria-hidden="true"><path d="M6 2h10v5H6zM2 8h18v8h-3v-3H5v3H2zm4 6h10v7H6zm2 2v1h6v-1zm0 2v1h6v-1z"/></svg>
      </div>
    </div>

    <div class="web-band">www.northgateroofworks.com</div>
  </section>

  <section class="logo-sheet" aria-label="Logo">
    <div class="wordmark">
      <span class="wordmark__mark"></span>
      <span class="wordmark__name">NORTHGATE<br>ROOFING WORKS</span>
    </div>
  </section>

</main>
</body>
</html>
```